The Bean Lantern - Looking for a stylish, cool, hipster style logo and website look and feel.

We need a logo and screen design for an e-commerce website that offers a variety of coffee blends to customers.
We first need a logo, and subsequently a theme for the entire website.
The design can be hipster/rustic/stylish, as it fits in the barrister/coffee culture environment. We are imagining a black/white logo and theme, which can also use an additional accent colour (we are open to suggestions).
In short, what we need: 1. A logo "The Bean Lantern", and a selection of fonts/accent colours for our platform.

Target Market(s)

Our target market is customers who shop coffee online. They are typically between 25 and 50 years old and value a very clean, crisp, stylish, professional design.

Industry/Entity Type

Coffee Shop

Contact Information for Business Card

logo, company name, more details to follow

Logo Text

The Bean Lantern

Number of Pages Required

1 page

Font styles to use
Sans Serif

Colors
474747
333333
000000
ffffff

Requirements
Must have
• Please note that the market we are operating in is very stylish. Some examples of the industry here:
• https://www.tallharbourroast.com.au/
• http://idaandmorton.com.au/
• It is essential that our design is stylish and cool.
Nice to have
• We are looking for a very stylish, cool, minimalistic (even hipster) look and feel.
• If more text is needed for a logo, you can add:
• Australia
• Australia's best roasters
• Speciality Coffee
Should not have
• Please no brown colour (as the association with coffee).

```html
<!DOCTYPE html>
<html lang="en">
<head>
<meta charset="utf-8">
<title>The Bean Lantern – Home</title>
<link href="https://fonts.googleapis.com/css2?family=Oswald:wght@500;700&family=Arimo:wght@400;700&family=Architects+Daughter&display=swap" rel="stylesheet">
<style>
  :root {
    --stage: #cbcbcb;
    --black: #000000;
    --ink: #111111;
    --grey-dark: #333333;
    --grey-mid: #474747;
    --grey-soft: #5a5a5a;
    --white: #ffffff;
    --mint: #6fdc9c;
    --mint-light: #8de6ae;
    --mint-deep: #58c888;
    --footer: #6f7a73;
    --coral: #e9826b;
    --coral-pale: #f6ddd3;
  }
  * { margin: 0; padding: 0; box-sizing: border-box; }
  html, body { width: 1200px; height: 1200px; overflow: hidden; }
  body { background: var(--stage); font-family: 'Arimo', Arial, sans-serif; position: relative; }
  .page { position: absolute; left: 135px; top: 0; width: 853px; height: 1200px; overflow: hidden; background: var(--white); }
  .abs { position: absolute; }

  /* header */
  .site-header { left: 0; top: 0; width: 853px; height: 150px; background: var(--black); }
  .brand { left: 20px; top: 14px; width: 160px; text-align: center; color: var(--white); }
  .brand-tagline { font-family: 'Oswald', sans-serif; font-weight: 500; font-size: 9px; letter-spacing: 1px; text-transform: uppercase; }
  .brand-mark { width: 44px; height: 44px; border: 2px solid var(--white); border-radius: 50%; margin: 12px auto 10px; }
  .brand-name { font-family: 'Oswald', sans-serif; font-weight: 500; font-size: 17px; letter-spacing: .5px; }
  .social-top { top: 13px; left: 672px; display: flex; gap: 22px; }
  .social-dot { width: 16px; height: 16px; border-radius: 50%; background: #8a8a8a; }
  .main-nav { top: 60px; left: 0; }
  .nav-item { position: absolute; font-family: 'Arimo', sans-serif; font-weight: 700; font-size: 14.5px; color: var(--white); white-space: nowrap; }
  .nav-item.is-active { color: var(--mint); }
  .nav-divider { position: absolute; top: -1px; width: 1px; height: 18px; background: #555; }

  .dropdown { left: 302px; top: 90px; width: 149px; height: 149px; background: var(--mint-light); opacity: .96; padding: 0 12px; z-index: 3; }
  .dropdown::before { content: ""; position: absolute; left: 72px; top: -7px; border: 7px solid transparent; border-top: 0; border-bottom-color: var(--mint-light); }
  .dropdown-title { font-size: 8px; font-weight: 700; color: var(--white); height: 23px; line-height: 23px; display: flex; align-items: center; gap: 6px; margin-left: -2px; }
  .dropdown-title i { width: 12px; height: 9px; border-radius: 50%; border: 2px solid var(--white); display: inline-block; }
  .dropdown-item { font-size: 8.5px; color: var(--white); height: 25.5px; line-height: 25.5px; border-top: 1px solid rgba(255,255,255,.45); }

  /* hero */
  .hero { left: 0; top: 150px; width: 853px; height: 407px; background: var(--white); box-shadow: inset 0 6px 6px -4px rgba(0,0,0,.2); }
  .hero-art { left: 324px; top: 11px; width: 529px; height: 396px;
    background: linear-gradient(135deg, var(--coral) 0%, #eea08b 50%, var(--coral-pale) 100%); }
  .hero-title { left: 32px; font-family: 'Oswald', sans-serif; font-weight: 700; font-size: 42px; line-height: 46px; letter-spacing: -.5px; text-transform: uppercase; white-space: nowrap; }
  .hero-title.line-one { top: 56px; color: var(--black); }
  .hero-title.line-two { top: 101px; color: var(--grey-soft); }
  .hero-copy { left: 32px; top: 158px; width: 272px; font-size: 13.7px; line-height: 21.8px; color: var(--ink); }
  .hero-rule { left: 32px; top: 257px; width: 270px; height: 1.5px; background: var(--ink); }
  .hero-sub { left: 32px; top: 268px; width: 270px; text-align: center; font-family: 'Oswald', sans-serif; font-weight: 500; font-size: 24px; line-height: 35px; color: var(--grey-dark); text-transform: uppercase; }
  .btn-blends { left: 83px; top: 347px; width: 168px; height: 38px; border-radius: 19px; background: var(--mint); border: 2px solid var(--mint-deep); color: var(--white); font-weight: 700; font-size: 11.5px; display: flex; align-items: center; justify-content: center; text-transform: uppercase; }
  .hero-arrow { left: 300px; top: 100px; }

  .tab { width: 58px; height: 29px; background: var(--white); z-index: 2; left: 399px; display: flex; justify-content: center; }
  .tab-down { top: 557px; border-radius: 0 0 29px 29px; align-items: flex-start; }
  .tab-down::after { content: ""; border: 9px solid transparent; border-top: 9px solid var(--mint); border-bottom: 0; }
  .tab-up { top: 969px; border-radius: 29px 29px 0 0; align-items: flex-end; }
  .tab-up::after { content: ""; border: 9px solid transparent; border-bottom: 9px solid var(--mint); border-top: 0; }

  /* products */
  .products { left: 0; top: 557px; width: 853px; height: 441px;
    background: linear-gradient(160deg, #4a4a4a 0%, #333 45%, #1b1b1b 100%); }
  .shop-ring { left: 80px; top: 71px; width: 274px; height: 274px; border-radius: 50%; background: #c3c3c3; display: flex; flex-direction: column; align-items: center; justify-content: center; font-family: 'Architects Daughter', cursive; color: var(--grey-soft); font-size: 36px; line-height: 46px; }
  .products-title { left: 359px; top: 95px; font-family: 'Oswald', sans-serif; font-weight: 700; font-size: 36px; color: var(--mint); text-transform: uppercase; white-space: nowrap; }
  .products-copy { left: 404px; top: 160px; width: 380px; font-size: 17.5px; line-height: 28px; color: #e2e2e2; }

  /* signup */
  .signup { left: 0; top: 998px; width: 853px; height: 123px; background: var(--black); border-top: 2px solid #777; }
  .signup-label { left: 48px; top: 14px; font-family: 'Architects Daughter', cursive; font-size: 11px; color: #cfcfcf; text-transform: uppercase; }
  .field { left: 44px; width: 200px; height: 19px; border-radius: 10px; background: var(--white); border: 2px solid #bdbdbd; font-size: 10px; color: #777; padding-left: 20px; line-height: 15px; }
  .field.username { top: 38px; }
  .field.email { top: 71px; }
  .signup-btn { left: 275px; top: 30px; width: 70px; height: 70px; border-radius: 50%; background: var(--white); border: 2px solid #bbb; display: flex; flex-direction: column; align-items: center; justify-content: center; font-family: 'Architects Daughter', cursive; font-size: 11px; color: var(--ink); }
  .signup-btn i { width: 22px; height: 12px; border: 1.5px solid var(--ink); border-radius: 0 0 11px 11px; margin-bottom: 4px; }
  .beans-art { left: 380px; top: 0; width: 473px; height: 121px; background: linear-gradient(90deg, #1a1a1a, #6a6a6a 30%, #777 60%, #6a6a6a); }

  /* footer */
  .site-footer { left: 0; top: 1121px; width: 853px; height: 79px; background: var(--footer); }
  .footer-col { top: 14px; }
  .footer-col h4 { font-family: 'Oswald', sans-serif; font-weight: 700; font-size: 11px; color: var(--black); text-transform: uppercase; margin-bottom: 3px; }
  .footer-col p { font-size: 6.5px; line-height: 10px; color: var(--black); }
  .footer-social { left: 590px; top: 39px; display: flex; gap: 14px; }
  .footer-social span { width: 14px; height: 14px; border-radius: 50%; background: #d6d6d6; }
  .footer-brand { left: 746px; top: 12px; width: 74px; text-align: center; font-family: 'Oswald', sans-serif; font-weight: 500; color: var(--black); }
  .footer-brand i { display: block; width: 22px; height: 22px; border: 1.5px solid var(--black); border-radius: 50%; margin: 0 auto 5px; }
  .footer-brand span { font-size: 8.5px; }
</style>
</head>
<body>
<div class="page">

  <header class="site-header abs">
    <div class="brand abs">
      <div class="brand-tagline">Australia's best roasters</div>
      <div class="brand-mark"></div>
      <div class="brand-name">The Bean Lantern</div>
    </div>
    <div class="social-top abs" aria-label="Social links">
      <span class="social-dot"></span><span class="social-dot"></span><span class="social-dot"></span><span class="social-dot"></span><span class="social-dot"></span>
    </div>
    <nav class="main-nav abs">
      <span class="nav-item is-active" style="left:305px">COFFEE
        <svg width="12" height="10" viewBox="0 0 12 10" style="margin-left:10px"><path d="M2 3l4 4 4-4" fill="none" stroke="#fff" stroke-width="2"/></svg>
      </span>
      <span class="nav-divider" style="left:398px"></span>
      <span class="nav-item" style="left:434px">SHOP</span>
      <span class="nav-divider" style="left:509px"></span>
      <span class="nav-item" style="left:546px">ABOUT US</span>
      <span class="nav-divider" style="left:654px"></span>
      <span class="nav-item" style="left:691px">CONTACT US</span>
    </nav>
  </header>

  <div class="dropdown abs">
    <div class="dropdown-title"><i></i>OUR COFFEE BLENDS</div>
    <div class="dropdown-item">Lorem ipsum dolor</div>
    <div class="dropdown-item">Sit amet consectetur</div>
    <div class="dropdown-item">Adipiscing</div>
    <div class="dropdown-item">Elitsed do</div>
    <div class="dropdown-item">Eiusmod</div>
  </div>

  <section class="hero abs">
    <div class="hero-art abs" role="img" aria-label="Watercolour illustration of a cappuccino cup on a saucer over an orange-red splash"></div>
    <h1 class="hero-title line-one abs">Best Roasters</h1>
    <h1 class="hero-title line-two abs">Best Coffee
      <svg width="44" height="32" viewBox="0 0 44 32" style="vertical-align:-2px"><ellipse cx="14" cy="17" rx="12" ry="9" fill="#111" transform="rotate(-35 14 17)"/><ellipse cx="31" cy="19" rx="11" ry="8" fill="#111" transform="rotate(30 31 19)"/></svg>
    </h1>
    <svg class="hero-arrow abs" width="150" height="90" viewBox="0 0 150 90"><path d="M5 40 C40 5 110 10 140 70" fill="none" stroke="#111" stroke-width="5" stroke-linecap="round"/><path d="M118 62 L142 74 L138 46" fill="none" stroke="#111" stroke-width="5" stroke-linecap="round" stroke-linejoin="round"/></svg>
    <p class="hero-copy abs">Lorem ipsum dolor sit amet, consectetur adipiscing elit, sed do eiusmod tempor incididunt ut labore et dolore magna aliqua. Ut enim ad minim veniam.</p>
    <div class="hero-rule abs"></div>
    <h2 class="hero-sub abs">Find out the Bean Lantern blends</h2>
    <div class="btn-blends abs">Our coffee blends</div>
  </section>
  <div class="tab tab-down abs"></div>

  <section class="products abs" role="img" aria-label="Dark photograph of roasted coffee beans on a wooden table">
    <div class="shop-ring abs">
      <span>SHOP</span><span>NOW !</span>
    </div>
    <h2 class="products-title abs">The Bean Lantern Products</h2>
    <p class="products-copy abs">Sed ut perspiciatis unde omnis iste natus error sit voluptatem accusantium doloremque laudantium, totam rem aperiam, eaque ipsa quae ab illo inventore veritatis et quasi architecto beatae vitae dicta sunt explicabo.</p>
  </section>
  <div class="tab tab-up abs"></div>

  <section class="signup abs">
    <div class="signup-label abs">Sign up to our coffee news</div>
    <div class="field username abs">User name</div>
    <div class="field email abs">Email</div>
    <div class="signup-btn abs"><i></i>SIGN UP</div>
    <div class="beans-art abs" role="img" aria-label="Sketched illustration of large coffee beans in grey"></div>
  </section>

  <footer class="site-footer abs">
    <div class="footer-col abs" style="left:53px"><h4>Coffee</h4><p>consequ magni<br>dolores<br>eos qui</p></div>
    <div class="footer-col abs" style="left:192px"><h4>Shop</h4><p>consequ magni<br>dolores<br>eos qui</p></div>
    <div class="footer-col abs" style="left:334px"><h4>About us</h4><p>consequ magni<br>dolores<br>eos qui</p></div>
    <div class="footer-col abs" style="left:491px"><h4>Contact us</h4><p>consequ magni<br>dolores<br>eos qui</p></div>
    <div class="footer-col abs" style="left:614px"><h4>Social media</h4></div>
    <div class="footer-social abs"><span></span><span></span><span></span><span></span><span></span></div>
    <div class="footer-brand abs"><i></i><span>The Bean Lantern</span></div>
  </footer>

</div>
</body>
</html>
```